Health Coach needs a Business Card Design

Need a really modern feminine business card design for a health and lifestyle coach. Needs to use geometric shapes, muted grey/blue/green pastels and black and white - see mood board attached and logo. The client likes black and white, modern, san serif with the use of lines and possibly a shadow leaf as in the mood board. Possibly put the tag line on the back or an icon of the logo. Logo is also attached. An icon of the logo would be great too.

Target Market(s)

Women (some men) aged 30 to 50.

Industry/Entity Type

Business

Contact Information for Business Card

Marla Teveny
e-mail: hello@marlatwell.example
website: marlatwell.example
Phone: +610497258316

The tag line is "Move well, live steady"

Font styles to use
Sans Serif

Colors
ecf7fb
cfeae6
000000
ffffff
f5f5f5

Requirements
Must have
• Black and white, logo, tag line and details
Nice to have
• Would be nice to incorporate the shadow palm.fern leaves as in the mood board and or geometric lines/shapes - see mood board. Could be either standard rectangle or would be happy with square too.
Should not have
• Flowers or decorations

```html
<!DOCTYPE html>
<html lang="en">
<head>
<meta charset="utf-8">
<title>marlatwell — Business Card</title>
<link href="https://fonts.googleapis.com/css2?family=Inter:wght@300;400&display=swap" rel="stylesheet">
<style>
  :root {
    --ink: #000000;
    --paper: #ffffff;
    --mint: #cfeae6;
    --stage: #d4d4d4;
    --logo-grey: #9a9a9a;
    --tag-grey: #8a8a8a;
  }
  * { margin: 0; padding: 0; box-sizing: border-box; }
  html, body {
    width: 1189px; height: 1200px; overflow: hidden;
    background: var(--stage);
    font-family: "Inter", Helvetica, Arial, sans-serif;
  }
  .card {
    position: absolute; left: 194px; width: 808px; height: 459px;
    background: var(--ink); overflow: hidden;
  }
  .card--front { top: 112px; }
  .card--back { top: 620px; }
  .card__shapes { position: absolute; inset: 0; width: 100%; height: 100%; }
  .brand { position: absolute; text-align: right; }
  .brand__name {
    font-weight: 300; color: var(--logo-grey);
    font-size: 38px; letter-spacing: 1px; line-height: 1;
  }
  .brand__tagline {
    font-weight: 300; color: var(--tag-grey);
    font-size: 12.5px; letter-spacing: 4.2px; text-transform: uppercase;
    margin-top: 16px;
  }
  .card--front .brand { right: 62px; top: 78px; }
  .card--back .brand { left: 0; right: 0; top: 208px; text-align: center; }
  .card--back .brand__name { font-size: 44px; }
  .card--back .brand__tagline { font-size: 16px; letter-spacing: 6px; margin-top: 20px; }
  .contact { position: absolute; right: 40px; top: 336px; list-style: none; }
  .contact__item {
    display: flex; align-items: center; justify-content: flex-end;
    color: var(--paper); font-weight: 300; font-size: 21.5px;
    height: 33px;
  }
  .contact__icon { width: 20px; height: 20px; margin-left: 26px; fill: var(--paper); }
  .holder {
    position: absolute; left: 63px; top: 404px;
    font-weight: 300; font-size: 23px; color: var(--ink);
  }
</style>
</head>
<body>
  <section class="card card--front">
    <svg class="card__shapes" viewBox="0 0 990 563" preserveAspectRatio="none" aria-hidden="true">
      <rect width="990" height="563" fill="var(--mint)"/>
      <path d="M282,0 C225,130 255,350 447,563 L990,563 L990,0 Z" fill="var(--ink)"/>
      <path d="M232,0 L282,0 C238,120 250,330 346,483 C248,390 188,180 232,0 Z" fill="var(--paper)"/>
    </svg>
    <div class="brand">
      <div class="brand__name">marlatwell</div>
      <div class="brand__tagline">Move well, live steady</div>
    </div>
    <ul class="contact">
      <li class="contact__item">+610497258316
        <svg class="contact__icon" viewBox="0 0 20 20"><circle cx="10" cy="6" r="4.5"/><path d="M1,19 C1,12 19,12 19,19 Z"/></svg>
      </li>
      <li class="contact__item">hello@marlatwell.example
        <svg class="contact__icon" viewBox="0 0 20 20"><rect x="1" y="3.5" width="18" height="13" fill="none" stroke="var(--paper)" stroke-width="1.6"/><path d="M1,4 L10,11 L19,4" fill="none" stroke="var(--paper)" stroke-width="1.6"/></svg>
      </li>
      <li class="contact__item">marlatwell.example
        <svg class="contact__icon" viewBox="0 0 20 20"><circle cx="10" cy="10" r="8.5"/><path d="M6,5 C9,6 8,9 11,10 C13,11 12,14 10,16 C8,14 6,12 5,9 Z M12,4 C14,5 15,7 14,8 C13,7 12,6 12,4 Z" fill="var(--ink)"/></svg>
      </li>
    </ul>
    <p class="holder">Marla Teveny</p>
  </section>

  <section class="card card--back">
    <div class="brand">
      <div class="brand__name">marlatwell</div>
      <div class="brand__tagline">Move well, live steady</div>
    </div>
  </section>
</body>
</html>
```